1 page marketing brochure for subcontractor services for Florida's Petroleum Contamination cleanup

I need a marketing brochure that can be emailed to potential clients to offer our comprehensive service capabilities to Agency Term Contractors in the Coastal Bureau of Habitat Stewardship's (CBHS) Fuel Recovery Initiative. We offer turnkey support from project management, monitoring, reporting, soil and groundwater assessment, remediation system engineering, design, construction, and system rental. We would like to see designs that use the green and goldish colors in our logo. I have attached the icon from our logo and an amateur in-house created design with some key points that are important to us. The icons used as bullet points can change. I've added examples of industry correct drilling icons. I also added a second picture of a system trailer in use. We are open to different Fonts and are open to assistance with copy refinement. This single page flyer is intended only for digital use (email/website) at this time.
Updates

Target Market(s)

Agency Term contractors in Coastal Bureau of Habitat Stewardship Fuel Recovery Initiative

Industry/Entity Type

Petroleum cleanup in Florida

Requirements
Should not have
• Don't show the Varnel name in the photo. See attached examples of industry appropriate drilling icons

```html
<!DOCTYPE html>
<html lang="en">
<head>
<meta charset="utf-8">
<title>Meridian – Your Subcontracting Partner</title>
<link href="https://fonts.googleapis.com/css2?family=Montserrat:ital,wght@0,500;0,700;0,800;1,500;1,600&family=Raleway:wght@400;500&display=swap" rel="stylesheet">
<style>
:root{
  --green:#146b3a;
  --gold:#b08d2e;
  --white:#ffffff;
  --stage:#e4e4e4;
  --photo-sky:#b9bfc6;
  --photo-mid:#a4a7a9;
  --photo-ground:#8a8d8f;
}
*{margin:0;padding:0;box-sizing:border-box}
html,body{width:1200px;height:1200px;overflow:hidden;background:var(--stage)}
body{font-family:"Raleway",sans-serif;color:var(--white)}
.flyer{position:absolute;left:176px;top:0;width:848px;height:1200px;background:var(--green);overflow:hidden}
.flyer-shapes{position:absolute;inset:0}
.flyer > div,.flyer > p,.flyer > h1,.flyer > h2,.flyer > ul{position:absolute}
.display{font-family:"Montserrat",sans-serif}
.brand{left:70px;top:110px;display:flex;align-items:center;gap:14px}
.brand-square{width:44px;height:44px;background:var(--green)}
.brand-name{font-family:"Montserrat",sans-serif;font-weight:800;font-size:30px;color:var(--green);letter-spacing:.5px}
.headline{left:54px;top:286px;font-family:"Montserrat",sans-serif;font-weight:800;font-size:33px;line-height:43px;letter-spacing:.5px}
.audience{left:54px;top:454px;font-weight:500;font-size:16px;line-height:22px;letter-spacing:.3px}
.turnkey{left:54px;top:518px;font-family:"Montserrat",sans-serif;font-weight:600;font-style:italic;font-size:18.5px}
.intro{left:54px;top:566px;width:510px;font-size:14.6px;line-height:20.5px}
.intro h2{font-family:"Montserrat",sans-serif;font-size:18.5px;font-weight:700;line-height:24px}
.intro p + p{margin-top:20.5px}
.anniversary{left:608px;top:548px;width:220px;text-align:center;font-family:"Montserrat",sans-serif}
.anniversary-number{display:block;font-weight:800;font-size:158px;line-height:150px;letter-spacing:-3px}
.anniversary-label{display:block;font-weight:500;font-style:italic;font-size:62px;line-height:62px;margin-top:-8px}
.services-title{left:54px;top:804px;font-family:"Montserrat",sans-serif;font-weight:800;font-size:18.5px}
.services-list{left:54px;top:833px;width:540px;list-style:none;display:grid;grid-template-columns:311px 229px;grid-template-rows:repeat(3,21px);grid-auto-flow:column;font-size:15px;line-height:21px;white-space:nowrap}
.why-title{left:54px;top:988px;font-family:"Montserrat",sans-serif;font-weight:800;font-size:18px}
.why-list{left:54px;top:1030px;list-style:none;font-size:15px;line-height:28.5px}
.why-list li{display:flex;align-items:center;gap:7px}
.why-list svg{width:10px;height:10px}
.mission-title{left:481px;top:988px;font-family:"Montserrat",sans-serif;font-weight:800;font-size:18px}
.mission-text{left:481px;top:1032px;font-size:15px;line-height:21px}
.contact{left:481px;top:1094px;list-style:none;font-size:15px;line-height:20.5px}
.contact li{display:flex;align-items:center;gap:16px}
.contact svg{width:10px;height:10px;fill:var(--white)}
</style>
</head>
<body>
<main class="flyer">
  <svg class="flyer-shapes" viewBox="0 0 848 1200" width="848" height="1200" aria-hidden="true">
    <polygon points="0,0 848,0 848,330 0,199" fill="var(--white)"/>
    <polygon points="533,456 848,530 848,840 618,840" fill="var(--gold)"/>
    <polygon points="0,900 426,997 426,1200 0,1200" fill="var(--gold)"/>
    <polygon points="426,0 848,0 848,512 426,414" fill="var(--white)"/>
    <defs>
      <linearGradient id="photoTone" x1="0" y1="0" x2="0" y2="1">
        <stop offset="0" stop-color="var(--photo-sky)"/>
        <stop offset=".55" stop-color="var(--photo-mid)"/>
        <stop offset="1" stop-color="var(--photo-ground)"/>
      </linearGradient>
    </defs>
    <polygon role="img" aria-label="Photo: drilling rig and crew working at a Varnel fuel station forecourt" points="426,0 848,0 848,500 426,402" fill="url(#photoTone)"/>
  </svg>

  <div class="brand">
    <span class="brand-square"></span>
    <span class="brand-name">MERIDIAN</span>
  </div>

  <h1 class="headline">YOUR<br>SUBCONTRACTING<br>PARTNER</h1>
  <p class="audience">FOR ATCs IN FLORIDA'S FUEL RECOVERY<br>INITIATIVE</p>
  <p class="turnkey">Offering Turnkey Project Support</p>

  <div class="intro">
    <h2>Partner with Experience you can Trust</h2>
    <p>With 40 years of service to CBHS and the Fuel Recovery Initiative, Meridian offers unmatched expertise in all phases of site assessment and remediation.</p>
    <p>For the new contract period, Meridian will not be an ATC and instead will be providing support to ATC firms by subcontracting our services to others. Meridian remains in good standing with CBHS and will continue to offer our high quality comprehensive service capabilities to ATCs across the state.</p>
  </div>

  <div class="anniversary">
    <span class="anniversary-number">40</span>
    <span class="anniversary-label">Years</span>
  </div>

  <h2 class="services-title">OUR SERVICES</h2>
  <ul class="services-list">
    <li>Project Management Support</li>
    <li>System Engineering &amp; Design</li>
    <li>System Construction, Rental &amp; O&amp;M</li>
    <li>Soil &amp; Groundwater Assessment</li>
    <li>Drilling &amp; Well Installation</li>
    <li>Monitoring &amp; Reporting</li>
  </ul>

  <h2 class="why-title">WHY CHOOSE MERIDIAN?</h2>
  <ul class="why-list">
    <li><svg viewBox="0 0 12 12"><path d="M1.5 6.5l3 3 6-7" fill="none" stroke="currentColor" stroke-width="2"/></svg>Comprehensive Capabilities</li>
    <li><svg viewBox="0 0 12 12"><path d="M1.5 6.5l3 3 6-7" fill="none" stroke="currentColor" stroke-width="2"/></svg>Recognized Top Performer</li>
    <li><svg viewBox="0 0 12 12"><path d="M1.5 6.5l3 3 6-7" fill="none" stroke="currentColor" stroke-width="2"/></svg>Deep Program Knowledge</li>
    <li><svg viewBox="0 0 12 12"><path d="M1.5 6.5l3 3 6-7" fill="none" stroke="currentColor" stroke-width="2"/></svg>Experienced In-house Personnel</li>
  </ul>

  <h2 class="mission-title">YOUR SUCCESS IS OUR MISSION</h2>
  <p class="mission-text">Together, we restore Florida's environment<br>safely - efficiently - effectively</p>
  <ul class="contact">
    <li><svg viewBox="0 0 12 12"><path d="M2.5 1l2 2.2-1 1.3a7 7 0 0 0 4 4l1.3-1 2.2 2-1.2 1.8C5.5 11 1 6.5 .7 2.2z"/></svg>863-555-0147</li>
    <li><svg viewBox="0 0 12 12"><path d="M0 2h12v8H0z"/></svg>contact@meridiansitelab.com</li>
    <li><svg viewBox="0 0 12 12"><circle cx="6" cy="6" r="5.5"/></svg>www.meridiansitelab.com</li>
  </ul>
</main>
</body>
</html>
```